Flyer or Info graphic required -for journey map/flow chart

I would like a info graphic designed around the Australian home buying process. explaining all the steps along the way and how it a fits together from the start all the way to settlement and when you pick up the keys.

i want it to be clear and simple. there is quite a lot of words and so the design needs to be simple so they can take it all in.
I have attached an example of one i have seen to give you an idea of what i am thinking as well as the required words

Target Market(s)

25-35 year old first time home buyers

Industry/Entity Type

Financial Service

Font styles to use
Sans Serif

Colors
0355a3

Requirements
Must have
• the word document attached called "start" has the steps i want in my document.
• there is also a hand drawn picture (untitled document) with a portion in yellow, this reflects a certain stage of the process called "cooling off" and it needs to be highlighted as one stage.
• there are also days mentioned on this document so readers understand how long things take
Nice to have
• Logo and Web Address & corporate colours

```html
<!DOCTYPE html>
<html lang="en">
<head>
<meta charset="utf-8">
<title>Home Buying Process</title>
<link href="https://fonts.googleapis.com/css2?family=Montserrat:wght@800&family=Fredoka:wght@500;600&family=Open+Sans:ital,wght@0,400;0,600;1,400&display=swap" rel="stylesheet">
<style>
  :root{
    --bg:#2f3238;
    --blue:#1c8fd9;
    --blue-dark:#1576bb;
    --sky:#3aa8ec;
    --red:#e8373a;
    --white:#ffffff;
  }
  *{box-sizing:border-box;margin:0;padding:0}
  html,body{width:848px;height:1200px;overflow:hidden;background:var(--bg)}
  .canvas{position:relative;width:848px;height:1200px;background:var(--bg);color:var(--white);font-family:"Open Sans",Arial,sans-serif}
  .abs{position:absolute}
  .hero-art{left:0;top:0;width:144px;height:78px;background:linear-gradient(135deg,var(--blue),var(--blue-dark));border-bottom-right-radius:40px}
  .title{left:0;width:848px;top:22px;text-align:center;font-family:"Montserrat",Arial,sans-serif;font-weight:800;font-size:40px;letter-spacing:1px}
  .banner{left:67px;top:82px;width:757px;height:34px;background:var(--blue);border-radius:12px;text-align:center;font-family:"Montserrat",Arial,sans-serif;font-weight:800;font-size:19px;line-height:34px;letter-spacing:.2px}
  .checklist{left:0;width:848px;top:130px;text-align:center;font-size:16px;letter-spacing:.3px}
  .checklist span{color:var(--sky)}
  .road{left:0;top:0}
  .num{width:30px;height:30px;border-radius:50%;background:var(--blue);border:3px solid var(--white);box-shadow:0 0 0 3px var(--bg);font-family:"Fredoka",Arial,sans-serif;font-weight:600;font-size:14px;line-height:24px;text-align:center}
  .step{font-family:"Fredoka",Arial,sans-serif;font-weight:600;font-size:15px;line-height:17px;text-align:center}
  .step.tight{font-size:14px;line-height:16px}
  .note{font-size:10px;line-height:13.4px}
  .note.center{text-align:center}
  .bullets{list-style:none}
  .bullets li{position:relative;padding-left:12px;margin-bottom:6px}
  .bullets li::before{content:"";position:absolute;left:0;top:5px;width:4px;height:4px;background:var(--sky)}
  .tip{color:var(--sky);font-style:italic;text-align:center;margin-top:4px}
  .day{height:15px;width:84px;background:var(--red);border-radius:8px;font-family:"Fredoka",Arial,sans-serif;font-weight:600;font-size:11px;line-height:15px;text-align:center}
  .start{left:784px;top:262px;width:40px;height:74px}
  .brand{left:626px;top:1086px;width:200px;font-family:"Fredoka",Arial,sans-serif;font-weight:600;font-size:26px;line-height:28px;color:var(--blue)}
</style>
</head>
<body>
<div class="canvas">

  <div class="abs hero-art" role="img" aria-label="Hand holding a set of house keys"></div>
  <svg class="abs" style="left:716px;top:36px" width="106" height="46" viewBox="0 0 106 46">
    <g fill="var(--blue)">
      <path d="M2 22 L26 4 L50 22 L46 22 L46 44 L6 44 L6 22 Z"/>
      <path d="M54 22 L78 4 L102 22 L98 22 L98 44 L58 44 L58 22 Z"/>
    </g>
    <g fill="var(--bg)">
      <rect x="13" y="26" width="7" height="7"/><rect x="31" y="26" width="7" height="7"/>
      <rect x="65" y="26" width="7" height="7"/><rect x="83" y="26" width="7" height="7"/>
    </g>
  </svg>

  <div class="abs title">HOME BUYING PROCESS</div>
  <div class="abs banner">OVERVIEW TO HELP INDER STAND ALL THE STEPS IN BUYING</div>
  <div class="abs checklist"><span>GET THE CHECKLIST FROM</span> WWW.SAMPLEHOMELOANS.EXAMPLE</div>

  <svg class="abs road" width="848" height="1200" viewBox="0 0 848 1200">
    <g fill="var(--blue)">
      <path d="M54 258 H780 V340 H106 V632 H54 A30 30 0 0 1 24 602 V288 A30 30 0 0 1 54 258 Z"/>
      <path d="M24 550 H790 A30 30 0 0 1 820 580 V872 A30 30 0 0 1 790 902 H24 Z"/>
      <path d="M54 820 H820 V902 H106 V1164 H54 A30 30 0 0 1 24 1134 V850 A30 30 0 0 1 54 820 Z"/>
      <path d="M24 1084 H562 V1164 H24 Z"/>
    </g>
    <rect x="106" y="632" width="634" height="188" fill="var(--bg)"/>
    <rect x="106" y="340" width="674" height="210" fill="var(--bg)"/>
    <rect x="106" y="902" width="714" height="182" fill="var(--bg)"/>
    <g fill="none" stroke="var(--bg)" stroke-width="7" stroke-linejoin="miter">
      <polyline points="572,256 552,299 572,342"/>
      <polyline points="324,256 304,299 324,342"/>
      <polyline points="116,256 96,299 116,342"/>
      <polyline points="20,392 65,414 110,392"/>
      <polyline points="140,548 160,591 140,634"/>
      <polyline points="348,548 368,591 348,634"/>
      <polyline points="516,548 536,591 516,634"/>
      <polyline points="716,548 736,591 716,634"/>
      <polyline points="736,664 780,686 824,664"/>
      <polyline points="736,794 780,816 824,794"/>
      <polyline points="652,818 632,861 652,904"/>
      <polyline points="444,818 424,861 444,904"/>
      <polyline points="244,818 224,861 244,904"/>
      <polyline points="116,818 96,861 116,904"/>
      <polyline points="20,946 65,968 110,946"/>
      <polyline points="20,1064 65,1086 110,1064"/>
      <polyline points="292,1082 312,1124 292,1166"/>
    </g>

    <g stroke="var(--white)" stroke-width="1" fill="none">
      <polyline points="282,242 282,258"/>
      <polyline points="358,242 358,258"/>
      <polyline points="614,240 614,258"/>
      <polyline points="218,438 218,550"/>
      <polyline points="232,436 218,436"/>
      <polyline points="412,436 412,550"/>
      <polyline points="426,436 412,436"/>
      <polyline points="654,424 654,550"/>
      <polyline points="668,424 654,424"/>
      <polyline points="40,680 30,680 30,860"/>
      <polyline points="696,702 720,702"/>
      <polyline points="696,766 740,766"/>
      <polyline points="158,776 168,776"/>
      <polyline points="158,776 158,820"/>
      <polyline points="142,938 130,938 130,980 106,980"/>
      <polyline points="456,928 464,928"/>
      <polyline points="456,902 456,938"/>
      <polyline points="680,902 680,938 686,938"/>
      <polyline points="126,1036 126,1084"/>
      <polyline points="132,1036 126,1036"/>
      <polyline points="340,1050 340,1084"/>
      <polyline points="352,1050 340,1050"/>
    </g>
    <g fill="var(--white)">
      <circle cx="232" cy="436" r="2.5"/><circle cx="426" cy="436" r="2.5"/><circle cx="668" cy="424" r="2.5"/>
      <circle cx="40" cy="680" r="2.5"/><circle cx="696" cy="702" r="2.5"/><circle cx="696" cy="766" r="2.5"/>
      <circle cx="168" cy="776" r="2.5"/><circle cx="142" cy="938" r="2.5"/><circle cx="464" cy="928" r="2.5"/>
      <circle cx="686" cy="938" r="2.5"/><circle cx="132" cy="1036" r="2.5"/><circle cx="352" cy="1050" r="2.5"/>
    </g>
    <g stroke="var(--red)" stroke-width="1.2" fill="none">
      <polyline points="472,522 472,550"/>
      <polyline points="472,522 478,522"/>
      <polyline points="112,902 112,917 134,917"/>
      <polyline points="106,996 142,996"/>
      <polyline points="656,902 656,1007 704,1007"/>
    </g>

    <g fill="none" stroke="var(--white)" stroke-width="2.4" stroke-linecap="round" stroke-linejoin="round">
      <circle cx="574" cy="302" r="12"/><path d="M574 302 V294 M574 302 L580 306 M570 287 H578"/>
      <rect x="338" y="280" width="26" height="34" rx="2"/><path d="M345 280 V276 H357 V280 M343 290 H358 M343 297 H358 M343 304 H352"/>
      <circle cx="362" cy="312" r="7" fill="var(--blue)"/><path d="M358 312 L361 315 L366 309"/>
      <path d="M46 284 H52 L58 306 H80 L84 290 H54"/><circle cx="61" cy="314" r="3"/><circle cx="78" cy="314" r="3"/>
      <path d="M82 590 L102 572 L122 590 M88 586 V610 H116 V586 M98 610 V598 H106 V610"/>
      <path d="M298 588 L318 580 V604 L298 596 Z M298 588 H292 V596 H298 M302 597 L305 608 M324 584 L330 580 M325 592 H333 M324 600 L330 604"/>
      <path d="M478 572 H500 L508 580 V612 H478 Z M484 586 H500 M484 594 H500 M484 602 H494 M496 604 L500 608 L508 598"/>
      <path d="M668 584 L688 572 L708 584 Z M672 588 V604 M681 588 V604 M695 588 V604 M704 588 V604 M666 608 H710"/>
      <path d="M764 586 L778 574 L792 586 V600 H764 Z M784 584 H798 V604 H784"/>
      <circle cx="780" cy="782" r="17"/><path d="M771 782 L778 789 L790 775"/>
      <circle cx="676" cy="861" r="22"/><path d="M676 847 V861 L686 869"/>
      <path d="M456 838 H478 L486 846 V884 H456 Z M462 852 H480 M462 860 H480 M462 868 H480 M462 876 H480"/>
      <path d="M250 848 H272 L280 856 V886 H250 Z M256 866 H274 M256 874 H274"/><circle cx="248" cy="848" r="8"/><path d="M242 854 L236 860"/>
      <path d="M100 852 L116 842 L132 852 V878 H100 Z M110 860 V876 L116 870 L122 876 V860 Z"/>
      <path d="M60 898 V886 M60 886 L46 874 M60 886 L74 874 M46 874 V880 M46 874 H52 M74 874 V880 M74 874 H68"/><circle cx="60" cy="902" r="4"/>
      <path d="M50 1024 H78 V1054 H56 A6 6 0 0 1 50 1048 Z M56 1034 H72 M56 1042 H72"/>
      <rect x="72" y="1108" width="30" height="22" rx="2"/><path d="M66 1134 H108"/>
      <path d="M352 1116 L380 1106 L392 1122 L364 1132 Z M352 1122 L364 1138 L392 1128 M352 1128 L364 1144 L392 1134"/>
    </g>
    <text x="87" y="1124" fill="var(--white)" font-family="Fredoka, sans-serif" font-weight="600" font-size="14" text-anchor="middle">$</text>
  </svg>

  <svg class="abs start" width="40" height="74" viewBox="0 0 40 74">
    <text x="14" y="66" fill="var(--white)" font-family="Montserrat, sans-serif" font-weight="800" font-size="18" transform="rotate(-90 14 66)">START</text>
    <g fill="var(--white)">
      <rect x="28" y="4" width="6" height="6"/><rect x="34" y="10" width="6" height="6"/>
      <rect x="28" y="16" width="6" height="6"/><rect x="34" y="22" width="6" height="6"/>
      <rect x="28" y="28" width="6" height="6"/><rect x="34" y="34" width="6" height="6"/>
      <rect x="28" y="40" width="6" height="6"/><rect x="34" y="46" width="6" height="6"/>
      <rect x="28" y="52" width="6" height="6"/><rect x="34" y="58" width="6" height="6"/>
    </g>
  </svg>

  <div class="abs step" style="left:594px;top:272px;width:170px">Time to start<br>“Living Like You Have a Mortgage”</div>
  <div class="abs step" style="left:380px;top:282px;width:140px">Get your Pre-<br>Approval in place</div>
  <div class="abs step" style="left:166px;top:282px;width:110px">Appoint your<br>Conveyancer</div>
  <div class="abs step" style="left:26px;top:332px;width:80px">Time to<br>go<br>shopping</div>
  <div class="abs step" style="left:24px;top:446px;width:84px">You<br>found the<br>Dream<br>Home -<br>Before<br>you make<br>an offer</div>
  <div class="abs step" style="left:186px;top:584px;width:110px">Make an offer</div>
  <div class="abs step" style="left:392px;top:574px;width:80px">Offer<br>Accepted</div>
  <div class="abs step tight" style="left:548px;top:562px;width:116px">Final<br>Instructions to<br>your Lender /<br>bank</div>
  <div class="abs step tight" style="left:740px;top:606px;width:80px">Strata<br>Report /<br>Building<br>Report</div>
  <div class="abs step" style="left:740px;top:718px;width:80px">Formal<br>Approval</div>
  <div class="abs step" style="left:700px;top:845px;width:100px">Cooling Off<br>Expires</div>
  <div class="abs step" style="left:492px;top:845px;width:136px">Lender Prepares<br>Loan Documents.</div>
  <div class="abs step tight" style="left:284px;top:830px;width:146px">Lender Reviews<br>Documents and is<br>“ready to book<br>settlement”</div>
  <div class="abs step" style="left:134px;top:845px;width:90px">Settlement<br>is Booked</div>
  <div class="abs step" style="left:24px;top:906px;width:84px">Cheque<br>Directions</div>
  <div class="abs step" style="left:24px;top:996px;width:84px">Settlement</div>
  <div class="abs step" style="left:118px;top:1108px;width:150px">Internet banking<br>and account set up</div>
  <div class="abs step" style="left:410px;top:1108px;width:120px">1st payment<br>is Due</div>

  <div class="abs num" style="left:742px;top:243px">1</div>
  <div class="abs num" style="left:525px;top:243px">2</div>
  <div class="abs num" style="left:283px;top:243px">3</div>
  <div class="abs num" style="left:61px;top:243px">4</div>
  <div class="abs num" style="left:14px;top:583px">5</div>
  <div class="abs num" style="left:231px;top:535px">6</div>
  <div class="abs num" style="left:430px;top:535px">7</div>
  <div class="abs num" style="left:534px;top:535px">8</div>
  <div class="abs num" style="left:719px;top:535px">9</div>
  <div class="abs num" style="left:805px;top:691px">10</div>
  <div class="abs num" style="left:805px;top:841px">11</div>
  <div class="abs num" style="left:591px;top:803px">12</div>
  <div class="abs num" style="left:398px;top:803px">13</div>
  <div class="abs num" style="left:117px;top:803px">14</div>
  <div class="abs num" style="left:57px;top:803px">15</div>
  <div class="abs num" style="left:7px;top:967px">16</div>
  <div class="abs num" style="left:7px;top:1103px">17</div>
  <div class="abs num" style="left:515px;top:1067px">18</div>

  <div class="abs day" style="left:478px;top:514px">DAY 1</div>
  <div class="abs day" style="left:134px;top:910px">DAY 40</div>
  <div class="abs day" style="left:142px;top:989px">DAY 42</div>
  <div class="abs day" style="left:704px;top:1000px">DAY 5</div>

  <p class="abs note center" style="left:106px;top:185px;width:200px">Make an appointment to talk to your Professional Mortgage Broker to discuss your Lender and Interest rate options and get the Pre-Approval under way</p>
  <p class="abs note center" style="left:354px;top:185px;width:192px">Make an appointment to talk to your Professional Mortgage Broker to discuss your Lender and Interest rate options and get the Pre-Approval under way</p>
  <p class="abs note center" style="left:586px;top:190px;width:180px">(it is a good idea a to talk to your Mortgage Broker to help set your savings target and find out how much you can borrow)</p>

  <ul class="abs note bullets" style="left:120px;top:403px;width:94px">
    <li>Have you done your research? Get a Property Profile report</li>
    <li>Ask the agent “what happens if my offer is accepted”</li>
  </ul>
  <ul class="abs note bullets" style="left:240px;top:356px;width:172px">
    <li>Remember this is not binding until you sign the contract and pay the deposit, your ‘just’ making an offer.</li>
    <li>Make sure your conveyancer has seen the contract before you sign it</li>
    <li>Remember – it is possible to also negotiate a smaller deposit (eg 5%) and longer cooling off period and or a longer Settlement period</li>
  </ul>
  <ul class="abs note bullets" style="left:440px;top:382px;width:196px">
    <li>Get the Contract and price to your Broker –make sure they know your Conveyancers Details.</li>
    <li>Sign the Contract &amp; pay your deposit (‘Normally’ 0.25% of the purchase price)</li>
    <li>Contracts are then “Exchanged” – and Cooling Off starts (normally 5 days)</li>
  </ul>
  <ul class="abs note bullets" style="left:678px;top:382px;width:146px">
    <li>Work with your broker to make sure they are correct and you understand all the documents before you sign.</li>
    <li>Your broker will instruct the Lender to proceed</li>
    <li>A Valuation is ordered</li>
  </ul>

  <div class="abs note" style="left:48px;top:656px;width:336px">
    <ul class="bullets">
      <li>This is where your Conveyancer checks exactly what has been paid, who needs to be paid and where the available money is sitting.</li>
      <li>If you have more savings to contribute they will give you the exact number.</li>
    </ul>
    <p class="tip">please make sure you ask them how to provide the funds. Eg can you transfer it to their Trust Account or do you need a bank cheque?</p>
  </div>
  <ul class="abs note bullets" style="left:168px;top:770px;width:170px">
    <li style="padding-left:14px">Your Conveyancer will coordinate this with your Lender and the Sellers Conveyancer</li>
  </ul>
  <ul class="abs note bullets" style="left:494px;top:648px;width:230px">
    <li>If you are buying a Unit – Talk to your conveyancer and get a strata report done.</li>
    <li>If you are buying a house – you need a “Pest &amp; Building Report”</li>
  </ul>
  <ul class="abs note bullets" style="left:494px;top:732px;width:230px">
    <li>When the Valuation is back (3 days) the bank will issue the Formal Approval</li>
    <li>Your broker will email you a copy and provide one to your Conveyancer</li>
  </ul>

  <ul class="abs note bullets" style="left:160px;top:930px;width:200px">
    <li>Your Conveyancer will contact you</li>
    <li>Pick up the keys for the Estate Agent</li>
    <li>Pizza party at your place!!!</li>
  </ul>
  <ul class="abs note bullets" style="left:464px;top:912px;width:190px">
    <li>Work with your broker to make sure they are correct and you understand all the documents before you sign.</li>
    <li>Return the signed documents to the Lender.</li>
  </ul>
  <ul class="abs note bullets" style="left:694px;top:913px;width:136px">
    <li>Now that you have your Approval and your reports are all ok, Cooling can expire and the Contract becomes “Formal”.</li>
  </ul>
  <ul class="abs note bullets" style="left:136px;top:1010px;width:170px">
    <li>This may take your Lender 7-10 days after settlement</li>
    <li>But you should be proactive and call them to set everything</li>
  </ul>
  <ul class="abs note bullets" style="left:360px;top:998px;width:250px">
    <li style="margin-bottom:3px">Normally 1 month after settlement</li>
    <li style="margin-bottom:3px">The Lender often messes this up – Call them to make sure it is set up how YOU want it</li>
    <li>Call them to set up a payment date that suits you – ie the day after your pay</li>
  </ul>

  <div class="abs brand">SAMPLE<br>HOME LOANS</div>
</div>
</body>
</html>
```